Stationery Refresh For Local Mortgage Broker

We want to modernise and standardise our stationery, including: letterhead, presentation folder, email signature and business card.

The new stationery should be a more modern and professional take on our existing colour scheme and brand. (We do not want a complete overhaul.) A folder of approved stock photos can be found here: https://files.cloudvaultex.com/share/7kTmQzR2wY9bLp4nVx3cHd8sJf6gNa1eU/view?usp=sharing

Our current website is: www.brellanfinco.com.au but we will be updating this to be consistent with our new stationery.

We are open to *very slight* tweaks to our logo if you feel it needs modernising, but overall we would like to maintain consistent colour scheme.

> Letterhead

418 Wenlock Parade,
Geelong, VIC, 3220
ABN: 37 158 402 963
Australian Credit License: 712893

(03) 5019 6284
www.brellanfinco.com.au

> Presentation Folder

418 Wenlock Parade,
Geelong, VIC, 3220
(03) 5019 6284
www.brellanfinco.com.au

ABN: 37 158 402 963

> Email Signature

Dylan Ferraway
Director
M. 0417 250 964
P. (03) 5019 6284
www.brellanfinco.com.au
418 Wenlock Parade,
Geelong, VIC, 3220

ABN: 37 158 402 963

(you can also include a photo if you like: https://brellanfinco.com.au/wp-content/uploads/2020/12/Dylan-Ferraway.png.webp)

> Business Card

Dylan Ferraway
Director
M. 0417 250 964
P. (03) 5019 6284
www.brellanfinco.com.au
418 Wenlock Parade,
Geelong, VIC, 3220

ABN: 37 158 402 963

Additional information...

If it's useful/relevant, the services we offer are: Home Loans, Investment Loans, Refinance, Debt Consolidation, Commercial Finance, Vehicle Loans
(You may choose to use this in any of the designs)

Target Market(s)

Home Buyers and Investors

Industry/Entity Type

Mortgage broking/property/real estate

Requirements
Must have
• At least somewhat consistent with our current site (yet meaningfully modernized)
Should not have
• dramatically different logo or colourscheme overhauls

```html
<!DOCTYPE html>
<html lang="en">
<head>
<meta charset="utf-8">
<title>Brellan Finance Co – Business Card</title>
<link rel="stylesheet" href="https://fonts.googleapis.com/css2?family=Arimo:wght@400;700&family=Montserrat:wght@400&display=swap">
<style>
  :root {
    --backdrop: #e4e4e2;
    --card-white: #f9f9f8;
    --card-dark: #262626;
    --brand-red: #a3141c;
    --ink-grey: #5a5a5a;
    --rule-grey: #8a8a8a;
    --emboss: #3a3a3a;
    --service-text: #f2f2f2;
  }
  * { margin: 0; padding: 0; box-sizing: border-box; }
  html, body { width: 1200px; height: 801px; overflow: hidden; }
  body {
    background: var(--backdrop);
    font-family: "Arimo", Arial, sans-serif;
    display: flex;
    align-items: center;
    justify-content: center;
    gap: 50px;
  }
  .card {
    position: relative;
    width: 525px;
    height: 300px;
    border-bottom: 4px solid var(--brand-red);
    box-shadow: 0 10px 24px rgba(0,0,0,0.18);
  }
  .card--front { background: var(--card-white); }
  .card--back { background: var(--card-dark); }

  /* front */
  .front-logo {
    position: absolute;
    left: 20px; top: 110px;
    width: 220px;
    text-align: center;
  }
  .wordmark {
    font-family: "Montserrat", Arial, sans-serif;
    font-weight: 400;
    font-size: 21px;
    letter-spacing: 5px;
    line-height: 1.35;
    color: var(--brand-red);
  }
  .front-divider {
    position: absolute;
    left: 255px; top: 40px;
    width: 1px; height: 170px;
    background: var(--rule-grey);
  }
  .contact {
    position: absolute;
    left: 280px; top: 40px;
    color: var(--ink-grey);
    font-size: 13px;
    line-height: 1.3;
  }
  .contact__name {
    color: var(--brand-red);
    font-weight: 700;
    font-size: 19px;
    line-height: 1.1;
  }
  .contact__role { margin-bottom: 12px; }
  .contact__address { margin-bottom: 12px; }
  .contact__line { display: flex; align-items: center; gap: 7px; }
  .contact__line svg { width: 11px; height: 11px; flex: none; }
  .front-footer {
    position: absolute;
    left: 0; right: 0; bottom: 26px;
    text-align: center;
    font-size: 13px;
    color: var(--ink-grey);
  }
  .front-footer b { font-weight: 700; }
  .front-footer .sep { margin: 0 8px; }

  /* back */
  .back-logo {
    position: absolute;
    left: 0; right: 0; top: 95px;
    text-align: center;
  }
  .back-logo .wordmark {
    color: var(--emboss);
    font-size: 26px;
    letter-spacing: 8px;
  }
  .services {
    position: absolute;
    left: 0; right: 0; bottom: 38px;
    text-align: center;
    color: var(--service-text);
    font-size: 14px;
    line-height: 1.6;
  }
  .services__item::before {
    content: "";
    display: inline-block;
    width: 6px; height: 6px;
    border-radius: 50%;
    background: var(--brand-red);
    margin: 0 6px 2px 10px;
    vertical-align: middle;
  }
</style>
</head>
<body>
  <section class="card card--front">
    <div class="front-logo">
      <div class="wordmark">BRELLAN<br>FINANCE CO</div>
    </div>
    <div class="front-divider"></div>
    <div class="contact">
      <div class="contact__name">Dylan Ferraway</div>
      <div class="contact__role">Director</div>
      <div class="contact__address">418 Wenlock Parade,<br>Geelong, VIC, 3220</div>
      <div class="contact__line">
        <svg viewBox="0 0 12 12" aria-hidden="true"><path fill="#a3141c" d="M2.5 1h2l1 2.6-1.3 1a6 6 0 0 0 3.2 3.2l1-1.3L11 7.5v2A1.5 1.5 0 0 1 9.5 11 8.5 8.5 0 0 1 1 2.5 1.5 1.5 0 0 1 2.5 1z"/></svg>
        <span>(03) 5019 6284</span>
      </div>
      <div class="contact__line">
        <svg viewBox="0 0 12 12" aria-hidden="true"><rect x="3" y="0.8" width="6" height="10.4" rx="1" fill="none" stroke="#a3141c" stroke-width="1.4"/><circle cx="6" cy="9.3" r="0.7" fill="#a3141c"/></svg>
        <span>0417 250 964</span>
      </div>
      <div class="contact__line">
        <svg viewBox="0 0 12 12" aria-hidden="true"><circle cx="6" cy="6" r="5" fill="none" stroke="#a3141c" stroke-width="1.3"/><path d="M1 6h10M6 1c-2 2.8-2 7.2 0 10M6 1c2 2.8 2 7.2 0 10" fill="none" stroke="#a3141c" stroke-width="1"/></svg>
        <span>www.brellanfinco.com.au</span>
      </div>
    </div>
    <div class="front-footer">
      <b>ABN:</b> 37 158 402 963<span class="sep">|</span><b>Australian Credit License:</b> 712893
    </div>
  </section>

  <section class="card card--back">
    <div class="back-logo">
      <div class="wordmark">BRELLAN<br>FINANCE CO</div>
    </div>
    <div class="services">
      <div><span class="services__item">Home Loans</span><span class="services__item">Investment Loans</span><span class="services__item">Refinance</span></div>
      <div><span class="services__item">Debt Consolidation</span><span class="services__item">Commercial Finance</span><span class="services__item">Vehicle Loans</span></div>
    </div>
  </section>
</body>
</html>
```